Commercial printing and sign company printed advertisement.

We're wanting a new look for our printed advertisements. We've been in business for 40 years and have been pushing hard the last couple of years to grow our business. Our target market is changing and our client base is changing. I am looking for advertisement that appeals to larger companies. However, we are not stuffy people so I would like the ads to convey our professionalism but also stand out with color and have a fun side. I'm currently needing advertisements for a printed magazine, printed newspaper, web ads and a table top at a local restaurant. We have our traditional four color logo (swoosh) as well as a simpler single color option. I am attaching various ads we have done previously so you can see what we have. It is important for these ads to convey the different things we do - as we do alot!

```html
<!DOCTYPE html>
<html lang="en">
<head>
<meta charset="UTF-8">
<title>K&amp;R Printing – A Printing &amp; Sign Company</title>
<link href="https://fonts.googleapis.com/css2?family=Open+Sans:wght@400;600&family=Syne:wght@500;700;800&display=swap" rel="stylesheet">
<style>
  :root {
    --tan-light: #d9ad6e;
    --tan: #c0935a;
    --tan-dark: #8f7150;
    --orange: #f39a33;
    --slate: #8a8394;
    --ink: #1c1a18;
    --brand-red: #c4492a;
    --press-teal: #2d6a80;
    --press-teal-dark: #1e4d5f;
    --white: #ffffff;
  }
  * { margin: 0; padding: 0; box-sizing: border-box; }
  html, body { width: 776px; height: 1200px; overflow: hidden; }
  body { background: var(--tan); font-family: "Syne", sans-serif; color: var(--ink); }

  .ad { position: relative; width: 776px; height: 1200px; overflow: hidden; }

  .ad__backdrop {
    position: absolute; inset: 0;
    background:
      radial-gradient(ellipse 60% 30% at 35% 22%, rgba(243,154,51,.75), transparent 70%),
      radial-gradient(ellipse 50% 25% at 80% 70%, rgba(243,154,51,.6), transparent 70%),
      radial-gradient(ellipse 40% 30% at 20% 65%, rgba(138,131,148,.35), transparent 70%),
      linear-gradient(160deg, var(--tan-light) 0%, var(--tan) 45%, var(--tan-dark) 100%);
  }

  .brand { position: absolute; left: 62px; top: 110px; }
  .brand__name {
    font-family: "Syne", sans-serif; font-weight: 700;
    font-size: 54px; line-height: 1; color: var(--brand-red);
  }
  .brand__tagline {
    font-family: "Open Sans", sans-serif; font-weight: 400;
    font-size: 20px; letter-spacing: .2px; margin: 12px 0 0 8px; color: var(--ink);
  }

  .headline {
    position: absolute; right: 78px; top: 304px; text-align: right;
    font-weight: 700; font-size: 19px; line-height: 22px;
  }

  .services {
    position: absolute; top: 420px; left: 59px;
    display: grid; grid-template-columns: 231px 231px 200px;
    font-weight: 500; font-size: 15.5px; line-height: 16.45px; letter-spacing: .8px;
  }
  .services ul { list-style: none; }
  .services li { white-space: nowrap; }

  .statement {
    position: absolute; left: 62px; top: 980px;
    font-weight: 700; font-size: 13.5px; color: #3a3530; white-space: nowrap;
  }

  .cta {
    position: absolute; left: 60px; top: 1019px; width: 639px; height: 137px;
    color: var(--white); text-align: center;
  }
  .cta__press {
    position: absolute; inset: 0;
    background: linear-gradient(90deg, var(--press-teal-dark), var(--press-teal) 45%, #5d8896 80%, #7a98a2);
  }
  .cta__text { position: relative; padding-top: 26px; }
  .cta__title { font-weight: 700; font-size: 18px; white-space: nowrap; }
  .cta__contact { margin-top: 12px; font-weight: 500; font-size: 12.5px; line-height: 15px; }
</style>
</head>
<body>
<main class="ad">
  <div class="ad__backdrop" role="img" aria-label="Abstract background of overlapping tan, orange and grey angular shards"></div>

  <header class="brand">
    <div class="brand__name">K&amp;R Printing</div>
    <div class="brand__tagline">A PRINTING &amp; SIGN COMPANY</div>
  </header>

  <h2 class="headline">Why shop anywhere else?<br>A Team You Can Trust Since 1985!</h2>

  <section class="services">
    <ul>
      <li>Admission Tickets</li><li>Awards/Trophies</li><li>Bags/Sacks</li><li>Balloons</li>
      <li>Banners</li><li>Binding</li><li>Blueprints</li><li>Booklets</li><li>Boxes</li>
      <li>Brochures</li><li>Bulk Mailers</li><li>Bumper Stickers</li><li>Business Cards</li>
      <li>Buttons</li><li>Calendars</li><li>Catalogs</li><li>Certificates</li><li>Coasters</li>
      <li>Coffee Mugs</li><li>Color Copies</li><li>CooziesCoupons</li><li>Cups</li><li>Decals</li>
      <li>Design</li><li>Digital Color</li><li>Door Hanger</li><li>Embroidery</li><li>Envelopes</li>
      <li>Fax Service</li><li>Flags</li><li>Flash Drives</li><li>Flashlights</li>
    </ul>
    <ul>
      <li>Flyers</li><li>Folders</li><li>Frisbees</li><li>Forms</li><li>Full Color Printing</li>
      <li>Funeral Programs</li><li>Golf Balls</li><li>Graphic Design</li><li>Invoices</li>
      <li>Invitations</li><li>Keychains</li><li>Labels</li><li>Laminating</li><li>Lanyards</li>
      <li>Letterhead</li><li>Logo Creation</li><li>Magazines</li><li>Mag. Calendars</li>
      <li>Magnetic Cards</li><li>Magnetic Signs</li><li>Mailing Services</li><li>Marketing Materials</li>
      <li>Matchbooks</li><li>Member Cards</li><li>Menus</li><li>Mousepads</li><li>Name Tags</li>
      <li>Napkins</li><li>Newsletters</li><li>Newspaper Inserts</li><li>Note Cards</li><li>Office Supplies</li>
    </ul>
    <ul>
      <li>Pencils</li><li>Pens</li><li>Plastic Footballs</li><li>Political Signs</li><li>Postcards</li>
      <li>Posters</li><li>Punch Cards</li><li>Raffle Tickets</li><li>Receipts</li>
      <li>Retractable Banner</li><li>Stands</li><li>Rubber Stamps</li><li>Scratchpads</li>
      <li>Screenprinting</li><li>Self-Inking Stamps</li><li>Signs of All Kinds</li><li>Stickers</li>
      <li>Sticky Notes</li><li>Stress Balls</li><li>Tab Dividers (Custom)</li><li>Table Tents</li>
      <li>Towels</li><li>Parcel Shipping</li><li>Vehicle Magnets</li><li>Vinyl Lettering</li>
      <li>Water Bottles</li><li>Wedding Invites</li><li>Wraps</li><li>Wristbands</li><li>Yo-Yos</li>
      <li>... and much more!</li>
    </ul>
  </section>

  <p class="statement">A COMMERCIAL PRINTING AND DESIGN COMPANY</p>

  <section class="cta">
    <div class="cta__press" role="img" aria-label="Close-up photo of a printing press in blue tones"></div>
    <div class="cta__text">
      <div class="cta__title">DON'T SEE IT?... JUST ASK!</div>
      <div class="cta__contact">555.014.2298<br>art@krprinting.com<br>www.krprinting.com</div>
    </div>
  </section>
</main>
</body>
</html>
```